I-71 Website for Washington D.C Cannabis Business

We need a website with a 21+ age (yes/no/captcha) verification
5 Pages listed on a top banner
Home/Splash Page-Should send back to splash & ask for 21+ veri
Shop-
about Us
Blog
Contact us:

Content for pages:
Splash Page - Contains How it works with 1-6 steps
1. Register for Rewards Or Head to {Link} for more anonymous Use
2. Choose Cookies & Free Gifts
3. Submit Address & Order
4.Recieve Confirmation Text
5.Send Separate Selfie and Clear Drivers License Picture
6.Enjoy Your Cookies and Free Gifts

Shop/Menu Page - Empty with top banner (will fill in this section)

Home- Should link back to Splash page
About Us-
"Welcome to Maple Parcel, where everyday is a maple day! We believe that everyone who chooses to enjoy the medicinal and relaxing benefits cannabis, should have safe and reliable access. And no matter your lifestyle or level of wellness, you deserve access to friendly customer service and professional courtesy. At Maple Parcel we provide Artisan Cookies that come with I-71 Gifted premium exotic cannabis + edibles & accessories. We provide an excellent variety of cookies and gifts, and all purchases improve your community!

For every 5 Cookies you purchase we donate 50 Sandwiches to Local DC Organizations that help our community members in need. In this way, you’ll be supporting the local DC community by purchasing from Maple Parcel (We also have Sandwich Rewards!!)

Maple Parcel is and always will be committed to providing DC The Best Service, Gifts & Experience. Always. We are committed to setting a standard for the gifting business in DC.

We appreciate you taking the time to check us out! We are here for all of your I-71 compliant needs.

Need to reach us? Please send all business related inquiries/compliments/complaints to Mapleparceldc@velnormail.com and we will reach out ASAP. We look forward to hearing from you!

-MP

Blog- This should be Fillable
Contact US: Should be fillable with text or graphic

Similar Websites to check out: https://www.dcqenlowfarm.com/
https://www.amberloftvista.com/

Target Market(s)

DC/Cannabis market

Coding

Coded - Design and coding required

Number of Pages Required

5+ page

Font styles to use
Other font styles liked:
• Sans Serif

Colors
0455a3
33b8a4
ffffff

Requirements
Must have
• 21+ age (yes/no/captcha) verification
I-71 Compliant
Color match the green to the logo
Nice to have
• I would like the website to have a fresh and fun look....without being corny
Cookie buttons (menu etc that look like a cookie)
Should not have
• No pictures of Marihuana

```html
<!DOCTYPE html>
<html lang="en">
<head>
<meta charset="utf-8">
<title>Maple Parcel – How It Works</title>
<link href="https://fonts.googleapis.com/css2?family=Questrial&display=swap" rel="stylesheet">
<style>
  :root{
    --blue:#0455a3;
    --teal:#33b8a4;
    --white:#ffffff;
    --lime:#0af012;
    --ink:#2a2a2a;
    --modal:#2b2b2b;
    --overlay:rgba(4,85,163,0.74);
  }
  *{box-sizing:border-box;margin:0;padding:0}
  html,body{width:724px;height:1200px;overflow:hidden;background:var(--white);font-family:"Questrial",sans-serif}
  .sprites{position:absolute;width:0;height:0;overflow:hidden}

  .screen{position:absolute;left:31px;width:662px;overflow:hidden}
  .screen--one{top:31px;height:330px}
  .screen--two{top:377px;height:387px}
  .screen--three{top:783px;height:387px}

  .hero-photo{position:absolute;inset:0}
  .hero-photo--dark{background:radial-gradient(ellipse at 60% 40%,#4a3627 0%,#2c211a 55%,#17110d 100%)}
  .hero-photo--warm{background:radial-gradient(ellipse at 60% 45%,#8a6d53 0%,#5e4a3b 50%,#3c3029 100%)}

  .requirements{position:absolute;right:0;top:0;width:288px;height:29px;background:var(--blue);border-bottom-left-radius:22px;display:flex;align-items:center;justify-content:flex-end;gap:8px;padding-right:42px}
  .requirement{display:flex;align-items:center;gap:4px;color:var(--white);font-size:6px;white-space:nowrap}
  .requirement svg{width:15px;height:15px}

  .brand{position:absolute;left:42px;top:22px;display:flex;align-items:center;gap:5px}
  .brand-mark{width:16px;height:16px;background:var(--lime);border-radius:2px}
  .brand-name{color:var(--white);font-size:9px;letter-spacing:.5px;line-height:1}
  .brand-tagline{color:var(--white);font-size:6px;margin-top:2px}

  .main-nav{position:absolute;right:43px;top:37px;display:flex;gap:12px}
  .main-nav a{color:var(--white);text-decoration:none;font-size:8px}

  .step-card{position:absolute;width:86px;height:90px;background:var(--white);border-radius:3px;overflow:hidden;text-align:center}
  .step-number{position:absolute;right:0;top:0;width:27px;height:26px;background:var(--teal);border-bottom-left-radius:22px;color:var(--white);font-size:11px;display:flex;align-items:center;justify-content:center;padding-left:3px}
  .step-icon{position:absolute;left:28px;top:21px;width:30px;height:32px}
  .step-label{position:absolute;left:4px;right:4px;top:59px;font-size:7px;line-height:10.5px;color:var(--ink)}

  .step-arrow{position:absolute;width:24px;height:8px}

  .shop-button{position:absolute;left:277px;width:107px;height:28px;background:var(--teal);border-radius:4px 4px 4px 12px;color:var(--white);font-size:8px;display:flex;align-items:center;justify-content:center;text-decoration:none}

  .site-footer{position:absolute;left:0;right:0;height:39px}
  .site-footer--lime{top:291px;background:var(--lime)}
  .footer-social{position:absolute;left:41px;display:flex;gap:5px}
  .footer-social span{width:19px;height:19px;border:1px solid var(--ink);display:block}
  .footer-social--light span{border-color:var(--white)}
  .footer-copy{position:absolute;left:0;right:0;text-align:center;font-size:7px}
  .footer-legal{position:absolute;right:43px;font-size:7px;display:flex;gap:4px}
  .footer-text-dark{color:var(--ink)}
  .footer-text-light{color:var(--white)}

  .footer-wave{position:absolute;left:0;top:300px;width:662px;height:87px}

  .age-overlay{position:absolute;inset:0;background:var(--overlay)}
  .age-modal{position:absolute;left:173px;top:126px;width:318px;height:134px;background:var(--modal);text-align:center;color:var(--white)}
  .age-title{font-size:29px;font-weight:400;margin-top:20px;letter-spacing:.3px;line-height:1}
  .age-text{font-size:9px;margin-top:8px}
  .age-confirm{position:absolute;left:94px;top:83px;width:129px;height:28px;background:var(--teal);color:var(--white);font-size:8px;display:flex;align-items:center;justify-content:center}
</style>
</head>
<body>

<svg class="sprites" aria-hidden="true">
  <defs>
    <symbol id="icon-tick" viewBox="0 0 16 16">
      <circle cx="8" cy="8" r="7" fill="none" stroke="#fff" stroke-width="1"/>
      <path d="M5 8.2l2 2 4-4.2" fill="none" stroke="#fff" stroke-width="1.4" stroke-linecap="round" stroke-linejoin="round"/>
    </symbol>
    <symbol id="icon-trophy" viewBox="0 0 32 32">
      <g fill="none" stroke="#0455a3" stroke-width="1.3" stroke-linejoin="round">
        <path d="M10 4h12v8a6 6 0 0 1-12 0z"/>
        <path d="M10 6H5a5 5 0 0 0 5 7M22 6h5a5 5 0 0 1-5 7"/>
        <path d="M16 18v5M12 23h8v3h-8zM9 26h14v3H9z"/>
        <path d="M16 7.5l1 2 2.2.3-1.6 1.5.4 2.2-2-1-2 1 .4-2.2-1.6-1.5 2.2-.3z"/>
      </g>
    </symbol>
    <symbol id="icon-gift" viewBox="0 0 32 32">
      <g fill="none" stroke="#0455a3" stroke-width="1.3" stroke-linejoin="round">
        <rect x="5" y="11" width="22" height="5"/>
        <rect x="6.5" y="16" width="19" height="13"/>
        <path d="M14 11v18M18 11v18"/>
        <path d="M16 11c-2-5-8-6-7-2 .5 2 4 2 7 2zM16 11c2-5 8-6 7-2-.5 2-4 2-7 2z"/>
      </g>
    </symbol>
    <symbol id="icon-list" viewBox="0 0 32 32">
      <g fill="none" stroke="#0455a3" stroke-width="1.3" stroke-linejoin="round">
        <rect x="7" y="4" width="18" height="26" rx="2"/>
        <path d="M13 4V2.5h6V4M13 7h6v4h-6z"/>
        <path d="M12 15h10M12 19h10M12 23h10M12 27h7M9 15h1M9 19h1M9 23h1"/>
      </g>
    </symbol>
    <symbol id="icon-mail" viewBox="0 0 32 32">
      <g fill="none" stroke="#0455a3" stroke-width="1.3" stroke-linejoin="round">
        <path d="M5 13l11-8 11 8v15H5z"/>
        <path d="M5 13l11 8 11-8M5 28l8-7M27 28l-8-7"/>
        <circle cx="16" cy="12" r="4"/>
        <path d="M14.3 12l1.2 1.2 2.3-2.4"/>
        <path d="M1 20h3M2 24h2"/>
      </g>
    </symbol>
    <symbol id="icon-idcard" viewBox="0 0 32 32">
      <g fill="none" stroke="#0455a3" stroke-width="1.3" stroke-linejoin="round">
        <rect x="2" y="6" width="28" height="21" rx="2"/>
        <path d="M2 10h28"/>
        <rect x="5" y="13" width="9" height="11"/>
        <path d="M17 14h10M17 18h10M17 22h7"/>
      </g>
    </symbol>
    <symbol id="icon-gifts" viewBox="0 0 32 32">
      <g fill="none" stroke="#0455a3" stroke-width="1.3" stroke-linejoin="round">
        <rect x="9" y="19" width="14" height="11"/>
        <path d="M7 15l14 4-1 3-14-4zM16 20v10"/>
        <path d="M12 16c-1-4 3-5 3-2M12 16c2-3 6-1 4 1"/>
        <path d="M22 5l.8 1.6 1.7.2-1.2 1.2.3 1.7-1.6-.8-1.6.8.3-1.7-1.2-1.2 1.7-.2zM28 12l.6 1.2 1.3.2-.9.9.2 1.3-1.2-.6-1.2.6.2-1.3-.9-.9 1.3-.2z"/>
        <circle cx="27" cy="4" r="1.5"/>
        <path d="M25 19c1-2 3-2 4-4"/>
      </g>
    </symbol>
    <symbol id="icon-arrow" viewBox="0 0 24 8">
      <path d="M0 4h22M18 1l4 3-4 3" fill="none" stroke="#fff" stroke-width="1"/>
    </symbol>
  </defs>
</svg>

<!-- Screen one: staggered steps -->
<section class="screen screen--one">
  <div class="hero-photo hero-photo--dark" role="img" aria-label="Close-up photo of chocolate chip cookies on a cooling rack"></div>

  <div class="requirements">
    <span class="requirement"><svg><use href="#icon-tick"/></svg>Be 21+</span>
    <span class="requirement"><svg><use href="#icon-tick"/></svg>Have a Valid ID</span>
    <span class="requirement"><svg><use href="#icon-tick"/></svg>Have a Valid Delivery Address</span>
  </div>
  <div class="brand">
    <span class="brand-mark"></span>
    <div><div class="brand-name">MAPLE PARCEL</div><div class="brand-tagline">Where Everyday is a Maple Day</div></div>
  </div>
  <nav class="main-nav"><a href="#">Home</a><a href="#">Shop</a><a href="#">Blog</a><a href="#">About</a><a href="#">Events</a><a href="#">New Page</a><a href="#">More</a></nav>

  <div class="step-card" style="left:42px;top:135px"><span class="step-number">01</span><svg class="step-icon"><use href="#icon-trophy"/></svg><p class="step-label">Register for Rewards</p></div>
  <div class="step-card" style="left:141px;top:110px"><span class="step-number">02</span><svg class="step-icon"><use href="#icon-gift"/></svg><p class="step-label">Choose Cookies &amp; Free Gifts</p></div>
  <div class="step-card" style="left:239px;top:135px"><span class="step-number">03</span><svg class="step-icon"><use href="#icon-list"/></svg><p class="step-label">Submit Address &amp; Order</p></div>
  <div class="step-card" style="left:337px;top:109px"><span class="step-number">04</span><svg class="step-icon"><use href="#icon-mail"/></svg><p class="step-label">Recieve Confirmation Text</p></div>
  <div class="step-card" style="left:436px;top:133px"><span class="step-number">05</span><svg class="step-icon" style="top:26px"><use href="#icon-idcard"/></svg><p class="step-label">Send Separate Selfie and Clear Drivers License Picture</p></div>
  <div class="step-card" style="left:535px;top:109px"><span class="step-number">06</span><svg class="step-icon"><use href="#icon-gifts"/></svg><p class="step-label">Enjoy Your Cookies and Free Gifts</p></div>

  <a class="shop-button" href="#" style="top:238px">CONTINUE TO SHOP</a>

  <footer class="site-footer site-footer--lime">
    <div class="footer-social" style="top:11px"><span></span><span></span><span></span><span></span></div>
    <p class="footer-copy footer-text-dark" style="top:18px">©2021 All Rights Reserved</p>
    <p class="footer-legal footer-text-dark" style="top:18px"><span>Privacy Policy</span><span>Cookie Policy</span></p>
  </footer>
</section>

<!-- Screen two: grid of steps -->
<section class="screen screen--two">
  <div class="hero-photo hero-photo--warm" role="img" aria-label="Close-up photo of chocolate chip cookies on a knit cloth"></div>

  <div class="requirements">
    <span class="requirement"><svg><use href="#icon-tick"/></svg>Be 21+</span>
    <span class="requirement"><svg><use href="#icon-tick"/></svg>Have a Valid ID</span>
    <span class="requirement"><svg><use href="#icon-tick"/></svg>Have a Valid Delivery Address</span>
  </div>
  <div class="brand">
    <span class="brand-mark"></span>
    <div><div class="brand-name">MAPLE PARCEL</div><div class="brand-tagline">Where Everyday is a Maple Day</div></div>
  </div>
  <nav class="main-nav"><a href="#">Home</a><a href="#">Shop</a><a href="#">Blog</a><a href="#">About</a><a href="#">Events</a><a href="#">New Page</a><a href="#">More</a></nav>

  <div class="step-card" style="left:166px;top:65px"><span class="step-number">01</span><svg class="step-icon"><use href="#icon-trophy"/></svg><p class="step-label">Register for Rewards</p></div>
  <div class="step-card" style="left:288px;top:65px"><span class="step-number">02</span><svg class="step-icon"><use href="#icon-gift"/></svg><p class="step-label">Choose Cookies &amp; Free Gifts</p></div>
  <div class="step-card" style="left:410px;top:65px"><span class="step-number">03</span><svg class="step-icon"><use href="#icon-list"/></svg><p class="step-label">Submit Address &amp; Order</p></div>
  <div class="step-card" style="left:166px;top:174px"><span class="step-number">04</span><svg class="step-icon"><use href="#icon-mail"/></svg><p class="step-label">Recieve Confirmation Text</p></div>
  <div class="step-card" style="left:288px;top:174px"><span class="step-number">05</span><svg class="step-icon" style="top:26px"><use href="#icon-idcard"/></svg><p class="step-label">Send Separate Selfie and Clear Drivers License Picture</p></div>
  <div class="step-card" style="left:410px;top:174px"><span class="step-number">06</span><svg class="step-icon"><use href="#icon-gifts"/></svg><p class="step-label">Enjoy Your Cookies and Free Gifts</p></div>

  <svg class="step-arrow" style="left:258px;top:104px"><use href="#icon-arrow"/></svg>
  <svg class="step-arrow" style="left:380px;top:104px"><use href="#icon-arrow"/></svg>
  <svg class="step-arrow" style="left:258px;top:215px"><use href="#icon-arrow"/></svg>
  <svg class="step-arrow" style="left:380px;top:215px"><use href="#icon-arrow"/></svg>

  <a class="shop-button" href="#" style="top:281px">CONTINUE TO SHOP</a>

  <svg class="footer-wave" viewBox="0 300 662 87" preserveAspectRatio="none" aria-hidden="true">
    <path d="M0 353C80 322 200 304 330 318C420 328 480 362 560 360C610 358 640 352 662 347V387H0Z" fill="#0455a3"/>
    <path d="M0 353C80 322 200 304 330 318C420 328 480 362 560 360C610 358 640 352 662 347" fill="none" stroke="#0af012" stroke-width="2.5"/>
  </svg>
  <div class="footer-social footer-social--light" style="top:354px"><span></span><span></span><span></span><span></span></div>
  <p class="footer-copy footer-text-light" style="top:369px">©2021 All Rights Reserved</p>
  <p class="footer-legal footer-text-light" style="top:369px"><span>Privacy Policy</span><span>Cookie Policy</span></p>
</section>

<!-- Screen three: age gate -->
<section class="screen screen--three">
  <div class="hero-photo hero-photo--warm" role="img" aria-label="Close-up photo of chocolate chip cookies on a knit cloth"></div>

  <div class="requirements">
    <span class="requirement"><svg><use href="#icon-tick"/></svg>Be 21+</span>
    <span class="requirement"><svg><use href="#icon-tick"/></svg>Have a Valid ID</span>
    <span class="requirement"><svg><use href="#icon-tick"/></svg>Have a Valid Delivery Address</span>
  </div>
  <div class="brand">
    <span class="brand-mark"></span>
    <div><div class="brand-name">MAPLE PARCEL</div><div class="brand-tagline">Where Everyday is a Maple Day</div></div>
  </div>
  <nav class="main-nav"><a href="#">Home</a><a href="#">Shop</a><a href="#">Blog</a><a href="#">About</a><a href="#">Events</a><a href="#">New Page</a><a href="#">More</a></nav>

  <div class="step-card" style="left:166px;top:65px"><span class="step-number">01</span><svg class="step-icon"><use href="#icon-trophy"/></svg><p class="step-label">Register for Rewards</p></div>
  <div class="step-card" style="left:288px;top:65px"><span class="step-number">02</span><svg class="step-icon"><use href="#icon-gift"/></svg><p class="step-label">Choose Cookies &amp; Free Gifts</p></div>
  <div class="step-card" style="left:410px;top:65px"><span class="step-number">03</span><svg class="step-icon"><use href="#icon-list"/></svg><p class="step-label">Submit Address &amp; Order</p></div>
  <div class="step-card" style="left:166px;top:174px"><span class="step-number">04</span><svg class="step-icon"><use href="#icon-mail"/></svg><p class="step-label">Recieve Confirmation Text</p></div>
  <div class="step-card" style="left:288px;top:174px"><span class="step-number">05</span><svg class="step-icon" style="top:26px"><use href="#icon-idcard"/></svg><p class="step-label">Send Separate Selfie and Clear Drivers License Picture</p></div>
  <div class="step-card" style="left:410px;top:174px"><span class="step-number">06</span><svg class="step-icon"><use href="#icon-gifts"/></svg><p class="step-label">Enjoy Your Cookies and Free Gifts</p></div>

  <svg class="step-arrow" style="left:258px;top:104px"><use href="#icon-arrow"/></svg>
  <svg class="step-arrow" style="left:380px;top:104px"><use href="#icon-arrow"/></svg>

  <a class="shop-button" href="#" style="top:281px">CONTINUE TO SHOP</a>

  <svg class="footer-wave" viewBox="0 300 662 87" preserveAspectRatio="none" aria-hidden="true">
    <path d="M0 353C80 322 200 304 330 318C420 328 480 362 560 360C610 358 640 352 662 347V387H0Z" fill="#0455a3"/>
    <path d="M0 353C80 322 200 304 330 318C420 328 480 362 560 360C610 358 640 352 662 347" fill="none" stroke="#0af012" stroke-width="2.5"/>
  </svg>
  <div class="footer-social footer-social--light" style="top:354px"><span></span><span></span><span></span><span></span></div>
  <p class="footer-copy footer-text-light" style="top:369px">©2021 All Rights Reserved</p>
  <p class="footer-legal footer-text-light" style="top:369px"><span>Privacy Policy</span><span>Cookie Policy</span></p>

  <div class="age-overlay"></div>
  <div class="age-modal" role="dialog" aria-labelledby="age-title">
    <h2 class="age-title" id="age-title">AGE VERIFICATION</h2>
    <p class="age-text">Please verify your age before shopping our products!</p>
    <a class="age-confirm" href="#">YES, I AM 21 OVER,</a>
  </div>
</section>

</body>
</html>
```